Home Services- Spring Clean Options

Brightfold Services provides a variety of Home Services- focused on cleaning & improving the exterior of the home:

 Power Washing- driveways, sidewalks, patios, decks, fence
 Fence Staining- make fence look new with variety of staining colors
 Gutter cleaning- important to make sure have proper Water Drainage
 Gutter Guard Installation- prevent damage to roof and house by keeping debris out of gutters and water flowing.
 Window Washing- our exterior washing team and reach the highest windows
 Landscape& Patio Lights- highlight areas for beauty and safety
Updates

We are are almost finished. Just please make sure you pay attention to the wording and grammer in Red thx

Target Market(s)

Middle to Upper level Home Owners (especially women)

Industry/Entity Type

Cleaning Services

Font styles to use
Serif
Sans Serif

Requirements
Must have
• Not be Cluttered- Clean friendly, professional look. Focus on the Professional

Info@TryBrightfoldServices.com
845-267-0000
Nice to have
• Pictures of services- these are just examples
Should not have
• Bigger and bolder Services & Specials. Want to Show all the Services we offer but do Not use too much detail- don't want it to look "cluttered"

```html
<!DOCTYPE html>
<html lang="en">
<head>
<meta charset="utf-8">
<title>Brightfold Services – Exterior Home Services Flyer</title>
<link rel="stylesheet" href="https://fonts.googleapis.com/css2?family=Poppins:wght@400;500;600;700;800&display=swap">
<style>
  :root {
    --navy: #1f2161;
    --navy-deep: #1a1c55;
    --heading-blue: #2c3e9f;
    --ink: #1c1f5a;
    --paper: #ffffff;
    --backdrop: #e4e5e8;
    --logo-grey: #d3d3d6;
    --ring-shadow: rgba(10, 12, 50, 0.35);
  }
  * { box-sizing: border-box; margin: 0; padding: 0; }
  html, body {
    width: 1200px; height: 989px; overflow: hidden;
    background: var(--backdrop);
    font-family: "Poppins", sans-serif;
  }
  .flyer {
    position: absolute; left: 268px; top: 24px;
    width: 665px; height: 940px;
    background: var(--paper);
    overflow: hidden;
    box-shadow: 0 4px 14px rgba(0,0,0,0.12);
  }
  .service-band {
    position: absolute; left: 417px; top: 0;
    width: 248px; height: 100%;
    background: var(--navy);
  }
  .brand-name {
    position: absolute; left: 50px; top: 48px;
    font-size: 21px; font-weight: 700; color: var(--logo-grey);
    letter-spacing: 0.2px;
  }
  .headline {
    position: absolute; left: 48px; top: 156px;
    font-weight: 800; font-size: 41px; line-height: 43px;
    color: var(--ink); letter-spacing: -0.5px;
  }
  .headline .accent { color: var(--heading-blue); }
  .tagline {
    position: absolute; left: 50px; top: 298px; width: 262px;
    border-top: 1.5px solid var(--heading-blue);
    border-bottom: 1.5px solid var(--heading-blue);
    padding: 5px 0 6px;
    font-size: 18.5px; font-weight: 500; color: var(--heading-blue);
    white-space: nowrap; letter-spacing: -0.2px;
  }
  .hero-photo {
    position: absolute; left: 22px; top: 389px;
    width: 324px; height: 358px;
    background: radial-gradient(ellipse at 55% 45%, #c9c4bd 0%, #9c8f80 35%, #f2f2f2 72%, #ffffff 100%);
  }
  .contact-card {
    position: absolute; left: 37px; top: 751px;
    width: 277px; height: 153px;
    background: var(--navy-deep);
    border-radius: 13px;
    color: var(--paper);
    padding: 14px 22px 0;
  }
  .contact-card .cta {
    font-size: 30px; font-weight: 500; line-height: 36px;
    padding-bottom: 8px;
    border-bottom: 1px solid rgba(255,255,255,0.8);
  }
  .contact-row {
    display: flex; align-items: center; gap: 10px;
    font-size: 14px; margin-top: 14px;
  }
  .contact-row + .contact-row { margin-top: 12px; }
  .contact-row svg { width: 20px; height: 20px; flex: none; }
  .contact-row.email { font-size: 12px; }
  .service {
    position: absolute; left: 343px;
    width: 250px; height: 144px;
    display: flex; align-items: center;
  }
  .service-ring {
    width: 144px; height: 144px; border-radius: 50%;
    background: var(--paper);
    border: 3px solid var(--navy);
    box-shadow: 6px 6px 12px var(--ring-shadow);
    display: flex; align-items: center; justify-content: center;
    flex: none;
  }
  .service-photo {
    width: 126px; height: 126px; border-radius: 50%;
  }
  .service-name {
    margin-left: 17px;
    color: var(--paper);
    font-size: 16.5px; font-weight: 700; line-height: 21px;
    text-transform: uppercase; white-space: nowrap;
  }
  .photo-power { background: linear-gradient(160deg, #7d8a6a 0%, #6f9a4e 45%, #c9c6bf 100%); }
  .photo-gutter { background: linear-gradient(180deg, #b9a894 0%, #8d8071 45%, #b3b5b8 100%); }
  .photo-window { background: linear-gradient(120deg, #6e98c4 0%, #c9ccd1 50%, #7d8189 100%); }
  .photo-fence { background: linear-gradient(180deg, #2f76c9 0%, #5f9a3e 45%, #b8612e 100%); }
  .photo-lights { background: radial-gradient(circle at 50% 60%, #a57845 0%, #4a3521 50%, #1b1d2c 100%); }
  .photo-guard { background: linear-gradient(180deg, #9ab0c8 0%, #8e8f8f 45%, #a0866a 100%); }
</style>
</head>
<body>
  <main class="flyer">
    <div class="service-band"></div>

    <div class="brand-name">Brightfold Services</div>

    <h1 class="headline">
      <span class="accent">FOCUSED ON</span><br>
      CLEANING &amp;<br>
      IMPROVING
    </h1>
    <p class="tagline">THE EXTERIOR OF THE HOME</p>

    <div class="hero-photo" role="img" aria-label="Smiling cleaner in apron and yellow gloves holding a bucket of cleaning supplies, giving a thumbs up"></div>

    <section class="contact-card">
      <p class="cta">CALL US NOW !</p>
      <p class="contact-row">
        <svg viewBox="0 0 20 20" aria-hidden="true"><circle cx="10" cy="10" r="10" fill="#fff"/><path d="M7.2 5.2c.4-.3.9-.2 1.1.2l.9 1.7c.2.4.1.8-.2 1.1l-.6.5c.5 1.2 1.3 2.1 2.5 2.7l.5-.6c.3-.3.8-.4 1.1-.2l1.6 1c.4.2.5.8.2 1.1-.9 1.2-2.1 1.5-3.4.8-2.3-1.2-3.8-3-4.5-5.4-.3-1.1.1-2.2.8-2.9z" fill="var(--navy-deep)"/></svg>
        845-267-0000
      </p>
      <p class="contact-row email">
        <svg viewBox="0 0 20 20" aria-hidden="true"><circle cx="10" cy="10" r="10" fill="#fff"/><rect x="5" y="6.5" width="10" height="7" rx="1" fill="none" stroke="var(--navy-deep)" stroke-width="1.3"/><path d="M5.3 7l4.7 3.6L14.7 7" fill="none" stroke="var(--navy-deep)" stroke-width="1.3"/></svg>
        Info@TryBrightfoldServices.com
      </p>
    </section>

    <div class="service" style="top:23px">
      <div class="service-ring"><div class="service-photo photo-power" role="img" aria-label="Worker power washing a concrete walkway beside a lawn"></div></div>
      <p class="service-name">Power<br>Washing</p>
    </div>
    <div class="service" style="top:176px">
      <div class="service-ring"><div class="service-photo photo-gutter" role="img" aria-label="Gutter filled with leaves and debris on a roof edge"></div></div>
      <p class="service-name">Gutter<br>Cleaning</p>
    </div>
    <div class="service" style="top:324px">
      <div class="service-ring"><div class="service-photo photo-window" role="img" aria-label="Man washing the exterior of a house window"></div></div>
      <p class="service-name">Window<br>Washing</p>
    </div>
    <div class="service" style="top:478px">
      <div class="service-ring"><div class="service-photo photo-fence" role="img" aria-label="Worker staining a wooden fence in a sunny yard"></div></div>
      <p class="service-name">Fence<br>Staining</p>
    </div>
    <div class="service" style="top:627px">
      <div class="service-ring"><div class="service-photo photo-lights" role="img" aria-label="Trees lit by landscape uplights at night"></div></div>
      <p class="service-name">Landscape &amp;<br>Patio Lights</p>
    </div>
    <div class="service" style="top:778px">
      <div class="service-ring"><div class="service-photo photo-guard" role="img" aria-label="Installer on a ladder fitting gutter guards on a house roofline"></div></div>
      <p class="service-name">Gutter Guard<br>Installation</p>
    </div>
  </main>
</body>
</html>
```